Consulting company requires a logo and business card design

I require a logo/business card design for a new company based in Sexsmith Alberta called TallMeadow Field Advisory Ltd. I plan to provide the following services: Construction management/inspection for the oil and gas industry, as well as general consulting for Asset Management, fleet management, etc. Have attached a copy of resume for use as guide for

Target Market(s)

Businesses within the oil and gas production, construction and shipping industry

Industry/Entity Type

Oil And Gas

Contact Information for Business Card

Believe should highlight, services offered, safety, quality,

Logo Text

TallMeadow Field Advisory (TMFA) ?

Font styles to use
Script

Requirements
Must have
• Open to all options

```html
<!DOCTYPE html>
<html lang="en">
<head>
<meta charset="utf-8">
<title>TallMeadow Field Advisory Ltd. – Business Card</title>
<link rel="stylesheet" href="https://fonts.googleapis.com/css2?family=Courgette&family=Open+Sans:wght@400&display=swap">
<style>
  :root {
    --backdrop: #2b2b2b;
    --card-grey: #505050;
    --panel-grey: #5a5a5a;
    --brand-blue: #559ad3;
    --ink-white: #ffffff;
    --shadow: rgba(0, 0, 0, 0.45);
  }
  * { margin: 0; padding: 0; box-sizing: border-box; }
  html, body {
    width: 1200px;
    height: 971px;
    overflow: hidden;
    background: var(--backdrop);
  }
  .sheet {
    position: relative;
    width: 1200px;
    height: 971px;
  }
  .card {
    position: absolute;
    left: 250px;
    width: 700px;
    height: 400px;
    overflow: hidden;
    box-shadow: 0 14px 30px var(--shadow);
  }
  .card--front { top: 60px; }
  .card--back { top: 510px; }
  .card svg.card-shapes {
    position: absolute;
    inset: 0;
    width: 700px;
    height: 400px;
    display: block;
  }
  .script {
    font-family: "Courgette", cursive;
    color: var(--ink-white);
  }
  .brand {
    position: absolute;
    left: 150px;
    top: 150px;
    display: flex;
    align-items: center;
    gap: 14px;
  }
  .brand-dot {
    width: 46px;
    height: 46px;
    border-radius: 50%;
    background: var(--ink-white);
    flex: none;
  }
  .brand-name {
    font-size: 24px;
    line-height: 1.2;
    width: 230px;
  }
  .tagline {
    position: absolute;
    right: 26px;
    bottom: 34px;
    width: 250px;
    font-size: 13px;
    line-height: 1.4;
    text-align: right;
  }
  .holder-name {
    position: absolute;
    left: 60px;
    top: 228px;
    font-size: 30px;
    white-space: nowrap;
  }
  .contact {
    position: absolute;
    display: flex;
    align-items: center;
    gap: 16px;
    white-space: nowrap;
  }
  .contact svg { flex: none; }
  .contact--address { left: 440px; top: 92px; }
  .contact--email { left: 420px; top: 190px; }
  .contact--phone { left: 460px; top: 288px; }
  .contact-text { font-size: 15px; line-height: 1.35; }
  .contact-text--email { font-size: 15px; }
  .contact-text--plain {
    font-family: "Open Sans", sans-serif;
    color: var(--ink-white);
    font-size: 17px;
    letter-spacing: 0.5px;
  }
</style>
</head>
<body>
<main class="sheet">

  <section class="card card--front" aria-label="Card front">
    <svg class="card-shapes" viewBox="0 0 700 400" aria-hidden="true">
      <rect width="700" height="400" fill="var(--card-grey)"/>
      <polygon points="80,50 650,50 560,260 120,350" fill="var(--brand-blue)"/>
      <polygon points="650,50 700,50 700,400 560,260" fill="var(--panel-grey)"/>
    </svg>
    <div class="brand">
      <span class="brand-dot"></span>
      <span class="brand-name script">TallMeadow Field Advisory Ltd.</span>
    </div>
    <p class="tagline script">Construction, quality assurance and maintenance management</p>
  </section>

  <section class="card card--back" aria-label="Card back">
    <svg class="card-shapes" viewBox="0 0 700 400" aria-hidden="true">
      <rect width="700" height="400" fill="var(--card-grey)"/>
      <rect x="0" y="180" width="460" height="130" fill="var(--brand-blue)"/>
      <polygon points="330,60 700,60 700,370 420,370" fill="var(--panel-grey)"/>
      <polygon points="370,165 700,165 700,255 400,255" fill="var(--brand-blue)"/>
    </svg>

    <p class="holder-name script">Daniel Whitcombe</p>

    <div class="contact contact--address">
      <svg width="36" height="32" viewBox="0 0 36 32" aria-hidden="true">
        <polygon points="18,2 34,16 29,16 29,30 21,30 21,21 15,21 15,30 7,30 7,16 2,16" fill="var(--ink-white)"/>
      </svg>
      <span class="contact-text script">RR#4 Brookfield Alberta,<br>T0K 2M0</span>
    </div>

    <div class="contact contact--email">
      <svg width="44" height="30" viewBox="0 0 44 30" aria-hidden="true">
        <rect x="6" y="2" width="32" height="21" rx="2" fill="none" stroke="var(--ink-white)" stroke-width="2.5"/>
        <path d="M1 26 H43 L40 29 H4 Z" fill="var(--ink-white)"/>
      </svg>
      <span class="contact-text contact-text--email script">dwhitcombe54@fieldmail.ca</span>
    </div>

    <div class="contact contact--phone">
      <svg width="24" height="38" viewBox="0 0 24 38" aria-hidden="true">
        <rect x="2" y="2" width="20" height="34" rx="3" fill="none" stroke="var(--ink-white)" stroke-width="2.5"/>
        <circle cx="12" cy="31" r="1.8" fill="var(--ink-white)"/>
      </svg>
      <span class="contact-text contact-text--plain">(780)555-0142</span>
    </div>
  </section>

</main>
</body>
</html>
```